Refresh Existing Tradeshow Expo Booth

Scope: We're looking for a refresh of our existing tradeshow booth materials.

Business: IT Company specializing in Education service and support of mobile technology. We repair, service and support schools Tevros, Quorvins, Nuvolettes and other technology.

Core Message: No-sign-ups, diagnostic fees, troubleshooting, or complicated invoicing. Just pack and ship, and we handle the rest.

Tagline: We make 1:1 repairs easy, fast, and affordable.

Additional Resources: https://www.quillbyte.net/for-education/

Deliverables:
1 - 72" x 30" Banner Stand
1 - 8' Table Cloth Throw
1 - 2.5' x 8' Banner
Included in .psd or .ai files ready to print.

Materials Provided:
Brand Usage Guide
Sample Flyers / Marketing Materials
Original Vertical Banner Stand / Banner
Sample Messaging

Target Market(s)

IT Directors, Education, ED Tech

Industry/Entity Type

IT, Education

Other font styles liked:
• Dekar, Dekar Light

Colors
EB3D1F
EC4F4E
F09395
F8D3D4
FCEDEE

Requirements
Must have
• Clean Design, Not Busy, Crisp Lines, Brand Colors.

```html
<!DOCTYPE html>
<html lang="en">
<head>
<meta charset="utf-8">
<title>Quillbyte – Banner Stand</title>
<link href="https://fonts.googleapis.com/css2?family=Anton&family=Saira:wght@300;400&family=Allura&display=swap" rel="stylesheet">
<style>
  :root {
    --page-bg: #e9edf0;
    --brand-red: #ed2024;
    --brand-red-soft: #f0393c;
    --ink: #222222;
    --ink-muted: #555555;
    --white: #ffffff;
  }
  html, body {
    margin: 0;
    padding: 0;
    width: 1200px;
    height: 1200px;
    overflow: hidden;
    background: var(--page-bg);
  }
  .banner {
    position: absolute;
    left: 320px;
    top: 30px;
    width: 561px;
    height: 1140px;
    background: var(--brand-red);
    overflow: hidden;
    box-shadow: 0 6px 24px rgba(0,0,0,0.15);
  }
  .banner__header {
    position: absolute;
    left: 0; top: 0;
    width: 100%;
    height: 142px;
    background: var(--white);
    display: flex;
    align-items: center;
    justify-content: center;
    gap: 18px;
  }
  .brand-dot {
    width: 74px;
    height: 74px;
    border-radius: 50%;
    background: var(--brand-red);
  }
  .brand-text { display: flex; flex-direction: column; }
  .brand-name {
    font-family: "Saira", sans-serif;
    font-weight: 300;
    font-size: 46px;
    letter-spacing: 5px;
    line-height: 1;
    color: var(--ink);
  }
  .brand-sub {
    font-family: "Saira", sans-serif;
    font-weight: 300;
    font-size: 17px;
    letter-spacing: 4px;
    color: var(--ink-muted);
    margin-top: 6px;
  }
  .banner__body {
    position: absolute;
    left: 0; top: 142px;
    width: 100%;
    height: 998px;
    background: radial-gradient(circle at 60% 40%, var(--brand-red-soft), var(--brand-red) 60%);
  }
  .headline-line {
    position: absolute;
    margin: 0;
    font-family: "Anton", sans-serif;
    font-weight: 400;
    color: var(--white);
    white-space: nowrap;
    line-height: 1;
    transform-origin: top left;
    text-transform: uppercase;
  }
  .headline-line--we-make { left: 76px; top: 33px; font-size: 120px; transform: scaleY(0.9); }
  .headline-line--repairs { left: 74px; top: 150px; font-size: 102px; transform: scaleY(0.95); }
  .headline-line--easy { left: 78px; top: 254px; font-size: 202px; transform: scaleY(0.97); }
  .headline-line--fast { left: 80px; top: 441px; font-size: 209px; transform: scaleY(0.91); }
  .headline-line--affordable { left: 83px; top: 721px; font-size: 84px; transform: scaleY(0.85); }
  .headline-script {
    position: absolute;
    left: 150px;
    top: 612px;
    margin: 0;
    font-family: "Allura", cursive;
    font-size: 135px;
    line-height: 1;
    color: var(--white);
  }
  .footer-mark {
    position: absolute;
    left: 0;
    top: 870px;
    width: 100%;
    display: flex;
    align-items: center;
    justify-content: center;
    gap: 14px;
  }
  .footer-mark__dot {
    width: 56px;
    height: 56px;
    border-radius: 50%;
    border: 3px solid var(--white);
    box-sizing: border-box;
  }
  .footer-mark__name {
    font-family: "Saira", sans-serif;
    font-weight: 300;
    font-size: 34px;
    letter-spacing: 4px;
    color: var(--white);
  }
</style>
</head>
<body>
  <main class="banner">
    <header class="banner__header">
      <div class="brand-dot"></div>
      <div class="brand-text">
        <span class="brand-name">QUILLBYTE</span>
        <span class="brand-sub">PHONE &amp; TABLET REPAIR</span>
      </div>
    </header>

    <section class="banner__body">
      <h1 class="headline-line headline-line--we-make">We Make</h1>
      <p class="headline-line headline-line--repairs">1:1 Repairs</p>
      <p class="headline-line headline-line--easy">Easy,</p>
      <p class="headline-line headline-line--fast">Fast,</p>
      <p class="headline-script">And</p>
      <p class="headline-line headline-line--affordable">Affordable.</p>

      <div class="footer-mark">
        <span class="footer-mark__dot"></span>
        <span class="footer-mark__name">QUILLBYTE</span>
      </div>
    </section>
  </main>
</body>
</html>
```